Update Financial Planning Presentation

We currently use a stock Powerpoint template. Information is imputed into an Excel spreadsheet and then linked to the presentation. We are looking to improve and upgrade this to a more straightforward and "cleaner" looking template. I have attached a sample copy of the Powerpoint presantation we currently use along with the Excel spreadsheet. I have attached our logo as well. Thanks.
Industry/Entity Type
Financial

```html
<!DOCTYPE html>
<html lang="en">
<head>
<meta charset="utf-8">
<title>Goals &amp; Objectives</title>
<link href="https://fonts.googleapis.com/css2?family=Montserrat:wght@400;500&family=Nunito+Sans:wght@400;600;800&display=swap" rel="stylesheet">
<style>
  :root {
    --bg: #f8f8f8;
    --ink: #222222;
    --text: #555555;
    --base: #444444;
    --leader: #8a8a8a;
    --green-dark: #2f7d32;
    --green-light: #58a14c;
    --badge: #2b2b2b;
    --blue: #3a86c4;
    --mint: #55d69e;
    --orange: #f0a52c;
    --pink: #e75f8b;
    --purple: #9d6db0;
    --red: #e0505a;
  }
  * { margin: 0; padding: 0; box-sizing: border-box; }
  html, body { width: 1200px; height: 900px; overflow: hidden; background: var(--bg); }
  .slide { position: relative; width: 1200px; height: 900px; background: var(--bg); font-family: "Nunito Sans", Arial, sans-serif; }
  .slide-art { position: absolute; inset: 0; width: 1200px; height: 900px; }
  .slide-number {
    position: absolute; left: 1130px; top: 14px; width: 40px; height: 34px;
    background: var(--badge); color: #fff; font: 500 18px/34px "Montserrat", sans-serif; text-align: center;
  }
  .slide-number::after {
    content: ""; position: absolute; left: 50%; bottom: -7px; margin-left: -7px;
    border-left: 7px solid transparent; border-right: 7px solid transparent; border-top: 7px solid var(--badge);
  }
  .slide-title {
    position: absolute; top: 95px; width: 100%; text-align: center;
    font: 500 40px/1 "Montserrat", sans-serif; letter-spacing: 3px; color: var(--ink);
  }
  .goal {
    position: absolute; transform: translateX(-50%); text-align: center; white-space: nowrap;
    color: var(--text); font-size: 19px; line-height: 26px;
  }
  .goal strong { font-weight: 800; }
  .goal-icon { display: inline-block; vertical-align: -4px; margin-right: 4px; }
  .goal--jane { left: 192px; top: 472px; }
  .goal--john { left: 317px; top: 393px; }
  .goal--income { left: 525px; top: 337px; }
  .goal--lifestyle { left: 767px; top: 310px; }
  .goal--portfolio { left: 942px; top: 240px; }
  .footer {
    position: absolute; top: 827px; width: 100%; text-align: center; color: var(--base);
    font-family: "Montserrat", sans-serif;
  }
  .footer-firm { font-size: 15.5px; font-weight: 500; letter-spacing: 0.4px; }
  .footer-contact { font-size: 14.5px; margin-top: 7px; letter-spacing: 0.3px; }
</style>
</head>
<body>
<main class="slide">
  <svg class="slide-art" viewBox="0 0 720 540" aria-hidden="true">
    <polygon points="512,0 720,0 720,72" fill="var(--green-dark)"/>
    <polygon points="600,0 720,0 720,40" fill="var(--green-light)"/>
    <g class="leaders" stroke="var(--leader)" stroke-width="0.8" stroke-dasharray="1.5 2">
      <line x1="119" y1="318" x2="119" y2="345"/>
      <line x1="208" y1="283" x2="208" y2="316"/>
      <line x1="340" y1="270" x2="340" y2="306"/>
      <line x1="479" y1="223" x2="479" y2="294"/>
      <line x1="575" y1="183" x2="575" y2="271"/>
    </g>
    <g class="peaks">
      <path d="M15 420 L108 354 Q120 345 132 354 L226 420 Z" fill="var(--blue)" fill-opacity="0.92"/>
      <path d="M103 420 L196 325 Q208 314 220 325 L313 420 Z" fill="var(--mint)" fill-opacity="0.85"/>
      <path d="M225 420 L328 315 Q340 303 352 315 L455 420 Z" fill="var(--orange)" fill-opacity="0.85"/>
      <path d="M353 420 L467 303 Q479 291 491 303 L605 420 Z" fill="var(--pink)" fill-opacity="0.85"/>
      <path d="M452 420 L563 280 Q575 266 587 280 L702 420 Z" fill="var(--purple)" fill-opacity="0.82"/>
    </g>
    <line x1="8" y1="421" x2="712" y2="421" stroke="var(--base)" stroke-width="2.5"/>
  </svg>

  <div class="slide-number">04</div>
  <h1 class="slide-title">GOALS &amp; OBJECTIVES</h1>

  <div class="goal goal--jane">
    <svg class="goal-icon" width="22" height="24" viewBox="0 0 22 24"><circle cx="11" cy="7" r="6" fill="var(--blue)"/><path d="M1 24 Q1 13 11 13 Q21 13 21 24 Z" fill="var(--blue)"/></svg>Jane to retire<br>at <strong>AGE 58</strong>
  </div>
  <div class="goal goal--john">
    <svg class="goal-icon" width="22" height="24" viewBox="0 0 22 24"><circle cx="11" cy="7" r="6" fill="var(--mint)"/><path d="M1 24 Q1 13 11 13 Q21 13 21 24 Z" fill="var(--mint)"/></svg>John to retire<br>at <strong>AGE 62</strong>
  </div>
  <div class="goal goal--income">
    <svg class="goal-icon" width="24" height="26" viewBox="0 0 24 26"><path d="M8 1 H16 L14 6 H10 Z" fill="var(--orange)"/><circle cx="12" cy="16" r="10" fill="var(--orange)"/><text x="12" y="21" text-anchor="middle" font-size="13" font-weight="800" fill="#fff" font-family="Nunito Sans, sans-serif">$</text></svg>Monthly Income at<br>Retirement of<br><strong>$7,000.00</strong><br><strong>in Today’s Dollars</strong>
  </div>
  <div class="goal goal--lifestyle">
    <svg class="goal-icon" width="38" height="26" viewBox="0 0 38 26"><rect x="9" y="1" width="20" height="6" fill="var(--red)"/><rect x="1" y="7" width="36" height="5" fill="var(--red)"/><rect x="4" y="12" width="30" height="14" fill="var(--red)"/><rect x="16" y="16" width="6" height="10" fill="#fff"/></svg>Maintain Current<br><strong>Lifestyle in Retirement</strong>
  </div>
  <div class="goal goal--portfolio">
    <svg class="goal-icon" width="22" height="26" viewBox="0 0 22 26"><rect x="2" y="2" width="12" height="16" fill="none" stroke="var(--purple)" stroke-width="2.5"/><rect x="8" y="8" width="12" height="16" fill="var(--bg)" stroke="var(--purple)" stroke-width="2.5"/></svg>Portfolio<br><strong>Management</strong>
  </div>

  <footer class="footer">
    <div class="footer-firm">TALLOWAY FINANCIAL SERVICES LTD ; LIFE INSURANCE &amp; FINANCIAL PLANNING</div>
    <div class="footer-contact">TELEPHONE 604-555-0182; FAX: 604-555-0183 E-MAIL: INFO@TALLOWAYFS.COM</div>
  </footer>
</main>
</body>
</html>
```